Website for a financial survey consultancy

WHO WE ARE
We're a niche HR consultancy specialising in salary comparison surveys for the financial asset management industry. We position ourselves as a small, highly responsive organisation with a strong personal relationship with each of our 50+ blue-chip clients.

WHAT WE DO
Our business is 80% surveys (= products), 20% consultancy (= services). The surveys are a set of online products which clients interact with to find the information they are interested in.

WHAT WE WANT
We are completely revising our existing marketing website and need a new up-to-date look and feel for the site. We want you to design 2 web pages
- Home page
- Internal content page

More details below in Must Have Priorities.

REFERENCE SITES
- www.pellimorn.com - nice background image
- www.vantrikel.com - ignoring the animations
- www.quorvalen.com
- www.lumiscap.com - clean, fresh, styly but prob not corporate enough
- www.dorvethfunds.com - spacious, beautiful, slightly dated tho
- www.thalbin.co.uk - ignore the colours. Like the simplicity, larger font size (although want to stick with sans-serif fonts for main content)

DELIVERABLES
The final designs should be delivered as one or more PSD files with clearly named layers. All design elements and treatments should be separated out, for example use adjustment layers rather than applied (and subsequently irreversible) adjustments, strokes, shading, etc.

WHAT NEXT
I'll be monitoring the contest every day and can respond to questions fast. You can IM me on Skype or MSN.
Updates

Project Deadline Extended
Reason: Hi folks,

I am extending the deadline to this project as I am travelling this week and therefore will not be able to make a final decision until next Monday. I will try and provide further feedback over the course of this week but I am only going to be online occasionally so be prepared to wait a few days for a reply from me.

Thanks for all the designs so far.

Owen

Target Market(s)

In order of importance, most important first

1. Potential customers - UK & US financial industry HR professionals, short on time. Heard about us already, want to find out more about what we do, confirm relevance for their needs. Core goal - establish credibility: are we properly resourced, will we be around for years to come, are we *real*.

2. Existing customers - UK & US financial industry professionals, short on time, under pressure, want results quickly, minimum faff, expect high quality, slickly presented information. Primary action: login and use surveys.

3. Industry professionals/researchers - probably arriving through blog content, looking to browse and hoover information. Valuable for their ability to spread awareness of who we are amongst their peers.

Industry/Entity Type

Financial

Requirements
Must have
• GENERAL
Style cues - Corporate, professional, financial, stylish, slick, clean, spacious, light
Size - standard 960px grid

NAVIGATION
- [ Home | About us | Surveys | Consulting | Blog ]
- Sub-nav (roll-over dropdown) on About Us, Surveys & Consulting

ALL PAGES
- Site navigation
- Client login (on screen permanently or link to ajaxy in-page pop-up)
- Footer section
- Existing logo (attached)* - this is obviously an important reference point in the design, esp colour

HOME PAGE
- Communicate (link thru to?) survey/consulting split
- Large photo(s)/backdrop (2-3 interchangeable options ideally). Please consider what rights agreement will be necessary for any photos you include in your design.
- Possibly bigger more prominent version of logo
- Strap line/sentence - "Focussed data is the key to success"
- 3 recent blog posts (should look good with and without blog post images)
- Free downloadable PDF research report + supporting blurb

INTERNAL PAGE
- Page title
- Content - typical page will be less than one screenfull
- Level 1 sub-heading
- Level 2 sub-heading
- Bulleted list
- Content supporting image (any image will do - interested in placement, borders (if any), spacing, caption, etc)
- 'Do something' button

* Note: there is some internal debate about this logo at the moment. Some (me) are keen for it to change, some (not me!) are not. If you have an web page design idea/concept that requires an evolution of the logo, go ahead and evolve it. We can explore this further in the design process as necessary, but don't sweat it.
Nice to have
• Values to communicate
- Knowledgeable
- Professional
- Secure
- Personal
- Experienced
- Financial industry specific
- Accurate
- Reliable
Should not have
• - Search box
- Social media links, other than RSS feed button (discrete)

```html
<!DOCTYPE html>
<html lang="en">
<head>
<meta charset="utf-8">
<title>Korvane Consulting – Home</title>
<link rel="stylesheet" href="https://fonts.googleapis.com/css2?family=Arimo:wght@400;700&family=Libre+Bodoni:ital@1&display=swap">
<style>
  :root {
    --navy: #17303d;
    --nav-dark: #1d3f55;
    --nav-rim: #d6e3ee;
    --panel: rgba(32, 58, 70, 0.93);
    --black: #000;
    --white: #fff;
    --footer: rgba(20, 20, 20, 0.94);
    --footer-muted: #9a9a9a;
    --orange-top: #ffc15a;
    --orange-bottom: #f59a12;
    --green: #2e9a16;
    --text-dark: #0b0b0b;
  }
  * { margin: 0; padding: 0; box-sizing: border-box; }
  html, body { width: 1200px; height: 720px; overflow: hidden; }
  body { font-family: "Arimo", Helvetica, Arial, sans-serif; position: relative; background: #a9c9dd; }

  .hero-backdrop {
    position: absolute; inset: 0;
    background:
      radial-gradient(ellipse 18% 45% at 62% 70%, rgba(120,145,180,0.35), transparent 75%),
      linear-gradient(180deg, transparent 0 90%, #8fa9b5 90% 91%, #6f8b96 91% 100%),
      radial-gradient(ellipse 60% 55% at 25% 60%, rgba(255,255,255,0.75), transparent 70%),
      linear-gradient(180deg, #7fb0d0 0%, #b7d6e6 35%, #e4eef2 65%, #cfdde3 90%);
  }

  .brand { position: absolute; left: 183px; top: 31px; width: 120px; }
  .brand-square { width: 120px; height: 116px; background: var(--navy); }
  .brand-name { margin-top: 10px; font-size: 34px; font-weight: 400; color: var(--navy); letter-spacing: 1px; }

  .main-nav {
    position: absolute; left: 655px; top: 31px; width: 499px; height: 36px;
    background: var(--nav-rim); border-radius: 18px; padding: 2px 8px;
  }
  .main-nav ul {
    list-style: none; display: flex; align-items: center; justify-content: space-around;
    height: 32px; background: linear-gradient(180deg, #2c5874, var(--nav-dark) 60%, #163246);
    border-radius: 16px; padding: 0 10px; color: var(--white); font-size: 14px;
  }

  .strapline {
    position: absolute; left: 176px; top: 424px;
    font-family: "Libre Bodoni", "Bodoni Moda", serif; font-style: italic;
    font-size: 27px; letter-spacing: 1px; color: var(--text-dark);
  }

  .sidebar {
    position: absolute; left: 834px; top: 93px; width: 317px; height: 627px;
    background: var(--panel); border-top: 6px solid var(--black); z-index: 2;
  }
  .sidebar-heading {
    position: absolute; left: -8px; width: 312px; height: 30px; background: var(--black);
    color: var(--white); font-size: 19px; font-weight: 400; padding-left: 33px; line-height: 30px;
  }
  .sidebar-heading::after {
    content: ""; position: absolute; left: 0; bottom: -8px;
    border-top: 8px solid var(--black); border-left: 8px solid transparent;
  }
  .heading-company { top: 15px; }
  .heading-blog { top: 232px; }
  .sidebar-text {
    position: absolute; left: 26px; width: 285px;
    color: var(--white); font-size: 13px; line-height: 16.9px; white-space: nowrap;
  }
  .company-text { top: 55px; }
  .blog-list { top: 289px; list-style: none; }
  .blog-list li { margin-bottom: 16.9px; }

  .report-cta { position: absolute; left: 30px; top: 552px; width: 270px; height: 80px; }
  .report-pill {
    position: absolute; left: 34px; top: 6px; width: 190px; height: 52px;
    background: linear-gradient(180deg, var(--orange-top), var(--orange-bottom));
    border: 2px solid #e8eef2; border-radius: 0 26px 26px 0;
    color: #111; text-align: center; padding: 6px 0 0 30px; line-height: 18px;
  }
  .report-pill .small { font-size: 14px; display: block; }
  .report-pill .large { font-size: 17px; display: block; }
  .report-disc { position: absolute; left: 0; top: 0; }
  .report-doc { position: absolute; left: 200px; top: -31px; }

  .site-footer {
    position: absolute; left: 0; top: 675px; width: 1200px; height: 45px;
    background: var(--footer); z-index: 1;
  }
  .footer-nav { position: absolute; left: 179px; top: 9px; color: var(--white); font-size: 12px; letter-spacing: 0.5px; word-spacing: 3px; }
  .footer-legal { position: absolute; left: 179px; top: 29px; color: var(--footer-muted); font-size: 9px; letter-spacing: 0.8px; }
</style>
</head>
<body>
  <div class="hero-backdrop" role="img" aria-label="Photo: man in a blue shirt, seen from behind, gazing at a wind turbine over a calm sea under a pale blue sky"></div>

  <div class="brand">
    <div class="brand-square"></div>
    <div class="brand-name">Korvane</div>
  </div>

  <nav class="main-nav">
    <ul>
      <li>Home</li><li>|</li>
      <li>About us</li><li>|</li>
      <li>Surveys</li><li>|</li>
      <li>Consulting</li><li>|</li>
      <li>Blog</li><li>|</li>
      <li>Contact Us</li>
    </ul>
  </nav>

  <p class="strapline">Focussed data is the key to success</p>

  <aside class="sidebar">
    <h2 class="sidebar-heading heading-company">Company</h2>
    <p class="sidebar-text company-text">Korvane Consulting specialises in compensa-<br>tion strategy and benchmarking, designing<br>performance management/reward systems<br>and HR solutions in asset management.<br>Our unique approach is characterised by<br>senior HR professionals with extensive<br>experience who provide practical HR<br>advice, and deliver reward and performance<br>solutions on time and within budget.</p>

    <h2 class="sidebar-heading heading-blog">Recent Blog Posts</h2>
    <ul class="sidebar-text blog-list">
      <li>Korvane Consulting specialises in compensa-<br>tion strategy and benchmarking, designing<br>performance management/reward systems<br>and HR solutions in asset management.</li>
      <li>Korvane Consulting specialises in compensa-<br>tion strategy and benchmarking, designing<br>performance management/reward systems<br>and HR solutions in asset management.</li>
      <li>Korvane Consulting specialises in compensa-<br>tion strategy and benchmarking, designing<br>performance management/reward systems<br>and HR solutions in asset management.</li>
    </ul>

    <a class="report-cta">
      <div class="report-pill"><span class="small">Collect your Free</span><span class="large">Research Report</span></div>
      <svg class="report-disc" width="70" height="70" viewBox="0 0 70 70" aria-hidden="true">
        <circle cx="35" cy="35" r="34" fill="#cfd6da" stroke="#555" stroke-width="1"/>
        <circle cx="35" cy="35" r="29" fill="#1f1f1f"/>
        <circle cx="35" cy="35" r="26" fill="var(--green)"/>
        <path d="M28 20h14v16h9L35 53 19 36h9z" fill="#e8f2e4"/>
      </svg>
      <svg class="report-doc" width="50" height="62" viewBox="0 0 50 62" aria-hidden="true">
        <path d="M2 2h34l12 12v46H2z" fill="#f4f4f4" stroke="#ccc"/>
        <path d="M36 2v12h12z" fill="#d3232b"/>
        <rect x="0" y="4" width="30" height="15" fill="#d3232b"/>
        <text x="4" y="15" font-family="Arimo, sans-serif" font-size="10" font-weight="700" fill="#fff">PDF</text>
        <rect x="8" y="26" width="32" height="2" fill="#c9c9c9"/>
        <rect x="8" y="32" width="32" height="2" fill="#c9c9c9"/>
        <rect x="8" y="38" width="24" height="2" fill="#c9c9c9"/>
        <rect x="28" y="44" width="16" height="12" fill="#f3b3b5"/>
      </svg>
    </a>
  </aside>

  <footer class="site-footer">
    <div class="footer-nav">Home &nbsp;| &nbsp;About us &nbsp;| &nbsp;Surveys &nbsp;| &nbsp;Consulting &nbsp;| &nbsp;Blog</div>
    <div class="footer-legal">Privacy Policy &nbsp;| &nbsp;Terms &amp; Conditions</div>
  </footer>
</body>
</html>
```